Business Card Design

The new Company is called The Harbor Pantry - based in Miami Beach, Florida and Connecticut. We want a business card to be catchy and memorable ( like our Company name). Our business is marketing and retail sales of flavored cashew nuts in boutique /high end stores. The new business card must include a logo which must be a cashew nut with a king's crown or Roman wreath.
Yes- we are looking for a logo to be designed for the business and for the business card.

Industry/Entity Type

Marketing

Font styles to use
Script

```html
<!DOCTYPE html>
<html lang="en">
<head>
<meta charset="utf-8">
<title>The Harbor Pantry – Business Card</title>
<link rel="stylesheet" href="https://fonts.googleapis.com/css2?family=Open+Sans:wght@400;600&family=Pinyon+Script&display=swap">
<style>
  :root {
    --backdrop: #d8d8d8;
    --card-white: #ffffff;
    --card-black: #0e0e0e;
    --card-black-soft: #1c1c1c;
    --gold: #d4ad5c;
    --gold-light: #f0d68e;
    --gold-dark: #b08a3e;
    --ink: #111111;
    --text-light: #f4f4f4;
    --divider: #8a8a8a;
  }
  * { margin: 0; padding: 0; box-sizing: border-box; }
  html, body {
    width: 1200px;
    height: 900px;
    overflow: hidden;
    background: var(--backdrop);
    font-family: "Open Sans", sans-serif;
  }
  .business-card {
    position: absolute;
    left: 160px;
    top: 200px;
    width: 880px;
    height: 500px;
    border-radius: 42px;
    overflow: hidden;
    background: var(--card-white);
    box-shadow: 0 18px 40px rgba(0, 0, 0, 0.18);
  }
  .brand-area {
    position: absolute;
    left: 0; top: 0;
    width: 100%;
    height: 310px;
    display: flex;
    flex-direction: column;
    align-items: center;
    padding-top: 56px;
  }
  .brand-dot {
    width: 120px;
    height: 120px;
    border-radius: 50%;
    background: var(--gold);
  }
  .brand-name {
    margin-top: 14px;
    font-family: "Pinyon Script", cursive;
    font-size: 64px;
    font-weight: 400;
    line-height: 1.2;
    color: var(--ink);
    white-space: nowrap;
  }
  .gold-band {
    position: absolute;
    left: 0; top: 310px;
    width: 100%;
    height: 12px;
    background: linear-gradient(90deg, var(--gold-dark), var(--gold-light) 45%, var(--gold) 75%, var(--gold-dark));
  }
  .contact-area {
    position: absolute;
    left: 0; top: 322px;
    width: 100%;
    height: 178px;
    background: radial-gradient(ellipse at 55% 60%, var(--card-black-soft), var(--card-black) 70%);
  }
  .holder {
    position: absolute;
    right: 412px;
    top: 46px;
    text-align: right;
    white-space: nowrap;
  }
  .holder-name {
    font-size: 32px;
    font-weight: 400;
    color: var(--gold);
    line-height: 1.2;
  }
  .holder-role {
    font-size: 21px;
    color: var(--text-light);
    line-height: 1.3;
  }
  .divider {
    position: absolute;
    left: 490px;
    top: 22px;
    width: 2px;
    height: 130px;
    background: var(--divider);
  }
  .contact-list {
    position: absolute;
    left: 512px;
    top: 22px;
    list-style: none;
    white-space: nowrap;
  }
  .contact-item {
    display: flex;
    align-items: center;
    height: 32px;
    font-size: 20px;
    color: var(--text-light);
  }
  .contact-icon {
    width: 24px;
    height: 24px;
    margin-right: 12px;
    flex: none;
  }
  .contact-icon * { fill: var(--gold); }
  .contact-icon .stroke { fill: none; stroke: var(--gold); stroke-width: 1.8; }
  .contact-icon .envelope-fold { fill: none; stroke: var(--card-black); stroke-width: 1.5; }
</style>
</head>
<body>
  <div class="business-card">
    <div class="brand-area">
      <div class="brand-dot"></div>
      <div class="brand-name">The Harbor Pantry</div>
    </div>

    <div class="gold-band"></div>

    <div class="contact-area">
      <div class="holder">
        <div class="holder-name">Milo Hart</div>
        <div class="holder-role">Managing Director</div>
      </div>

      <div class="divider"></div>

      <ul class="contact-list">
        <li class="contact-item">
          <svg class="contact-icon" viewBox="0 0 24 24" aria-hidden="true">
            <path d="M12 3 L2 12 H5 V21 H10 V15 H14 V21 H19 V12 H22 Z"/>
          </svg>
          PO Box 40915 FL 33139
        </li>
        <li class="contact-item">
          <svg class="contact-icon" viewBox="0 0 24 24" aria-hidden="true">
            <path d="M6.6 10.8c1.4 2.8 3.8 5.1 6.6 6.6l2.2-2.2c.3-.3.7-.4 1-.2 1.1.4 2.3.6 3.6.6.6 0 1 .4 1 1V20c0 .6-.4 1-1 1C10.6 21 3 13.4 3 4c0-.6.4-1 1-1h3.5c.6 0 1 .4 1 1 0 1.3.2 2.5.6 3.6.1.3 0 .7-.2 1z"/>
          </svg>
          1305 778 902
        </li>
        <li class="contact-item">
          <svg class="contact-icon" viewBox="0 0 24 24" aria-hidden="true">
            <path d="M2 9 L12 3 L22 9 V20 H2 Z"/>
            <path class="envelope-fold" d="M4 10 L12 15 L20 10"/>
          </svg>
          Milo@harborpantry.com
        </li>
        <li class="contact-item">
          <svg class="contact-icon" viewBox="0 0 24 24" aria-hidden="true">
            <circle class="stroke" cx="12" cy="12" r="9.5"/>
            <ellipse class="stroke" cx="12" cy="12" rx="4.2" ry="9.5"/>
            <line class="stroke" x1="2.5" y1="12" x2="21.5" y2="12"/>
            <line class="stroke" x1="12" y1="2.5" x2="12" y2="21.5"/>
          </svg>
          www.harborpantry.com
        </li>
      </ul>
    </div>
  </div>
</body>
</html>
```